Shopping Web Site

I am looking for a retail website for my Curry Powder Business, I only sell 3 or 4 items so just need a simple website design with checkout but colours are important as I need Indian orange, red, green colours, we will email more info to the successful party. Attached is our logo and you can Social Rovin Pantry to get more information. Thanks

Industry/Entity Type

Business

```html
<!DOCTYPE html>
<html lang="en">
<head>
<meta charset="utf-8">
<title>Rovin Pantry — Shop</title>
<link rel="stylesheet" href="https://fonts.googleapis.com/css2?family=Arimo:wght@400;700&family=Carlito&family=Varela+Round&display=swap">
<style>
:root{
  --red:#c33a2e;
  --orange:#f7941d;
  --orange-deep:#f08a10;
  --green:#5cbf68;
  --green-dark:#2f8f3f;
  --ink:#1c1c1c;
  --muted:#555;
  --footer:#efefef;
  --card:#222;
  --field:#d4d4d4;
  --link:#2a9fd6;
}
*{box-sizing:border-box;margin:0;padding:0}
html,body{width:844px;height:1200px;overflow:hidden;background:#fff}
body{position:relative;font-family:"Arimo",Arial,sans-serif;color:var(--ink)}
.abs{position:absolute}

/* header */
.brand{left:27px;top:10px;display:flex;align-items:center;gap:8px;font-size:17px;font-weight:700;color:var(--red)}
.brand-dot{width:22px;height:22px;border-radius:50%;background:var(--red)}
.care{left:475px;top:5px;font-size:10px}
.care strong{font-size:14px;margin-left:6px}
.top-link{top:29px;font-size:9px}
.basket{left:475px;top:43px;width:172px;height:22px;border:1px solid #e3e3e3;display:flex;align-items:center;padding-left:6px}

/* nav */
.nav{left:21px;top:71px;width:802px;height:32px;background:var(--red);display:flex;align-items:center;padding-left:43px;gap:26px}
.nav a{color:#fff;font-size:11px;text-decoration:none}

/* register panel */
.register{left:699px;top:47px;width:124px;height:142px;background:#fff;box-shadow:0 1px 5px rgba(0,0,0,.3);border-radius:2px;z-index:3;text-align:center;padding-top:8px}
.register h3{font-size:11px;font-weight:400;margin-bottom:8px}
.register .field{width:100px;height:13px;margin:0 auto 8px;background:var(--field);border-radius:2px;font-size:7px;line-height:13px;color:#333}
.register .btn{width:100px;height:15px;margin:0 auto 8px;background:var(--orange);color:#fff;font-size:7px;line-height:15px;border-radius:2px}
.register .member{font-size:7px;color:var(--orange)}

/* hero */
.hero{left:21px;top:104px;width:802px;height:280px;background:linear-gradient(90deg,var(--orange-deep),var(--orange) 60%,#f9a53a)}
.hero h1{position:absolute;left:40px;top:34px;font-family:"Varela Round",sans-serif;font-weight:400;color:#fff;font-size:34px;line-height:44px}
.hero-photo{position:absolute;left:419px;top:3px;width:230px;height:274px;background:radial-gradient(ellipse at 50% 60%,#8a5a2c,#5d3a1d 55%,#e7d7c0 100%);opacity:.9}
.play{position:absolute;left:49px;top:227px;width:26px;height:26px;border-radius:50%;background:rgba(255,255,255,.55)}

/* why */
.why-title{left:61px;top:404px;font-size:27px;font-weight:400}
.feature{top:450px;width:220px}
.feature h4{font-size:12px;font-weight:400;margin-bottom:12px}
.feature .row{display:flex;gap:14px}
.feature svg{flex:none;margin-left:10px}
.feature p{width:162px;font-size:9.5px;line-height:12px;text-align:justify}

/* products */
.products{left:21px;top:587px;width:802px;height:360px;background:var(--green)}
.products h2{position:absolute;top:28px;width:100%;text-align:center;font-family:"Carlito",sans-serif;font-weight:400;font-size:26px;color:#fff}
.card{position:absolute;top:93px;width:214px}
.card .shot{height:196px;background:var(--card);position:relative}
.card .shot .pic{position:absolute;left:30px;top:10px;width:154px;height:160px}
.card .caption{position:absolute;bottom:5px;width:100%;text-align:center;color:#fff;font-size:10px;line-height:11px}
.card .price{text-align:right;font-size:10px;font-weight:700;color:#fff;margin-top:3px}
.card .more{margin-top:6px;margin-left:10px;font-size:17px;color:#fff;display:flex;align-items:center;gap:8px}

/* newsletter */
.news-title{left:109px;top:955px;font-size:29px;font-weight:700}
.news-input{left:453px;top:960px;width:194px;height:32px;background:var(--green);color:#4f9e57;font-size:11px;padding:10px 12px}
.news-btn{left:647px;top:960px;width:85px;height:32px;background:var(--green-dark);color:#fff;font-size:11px;line-height:32px;text-align:center}

/* footer */
.footer{left:0;top:1029px;width:844px;height:171px;background:var(--footer)}
.foot-head{top:22px;font-size:9px;font-weight:700;color:#444}
.foot-rule{top:38px;height:1px;background:#d5d5d5}
.tweet{left:44px;font-size:8px;color:#333;line-height:10px}
.tweet .url{color:var(--link);font-size:6px}
.tweet .when{color:#e07a9a;font-size:6px}
.fb-box{left:227px;top:45px;width:196px;height:98px;background:#fff;border:1px solid #ddd}
.avatars{position:absolute;left:4px;top:6px;display:flex;gap:4px}
.avatar{width:34px;text-align:center;font-size:6px;color:#555}
.avatar span{display:block;width:34px;height:34px;background:linear-gradient(#b78a6b,#6e4f3c);margin-bottom:2px}
.fb-note{position:absolute;left:6px;top:58px;font-size:6px;color:#555}
.like{position:absolute;right:6px;bottom:6px;width:32px;height:13px;background:#5b74a8;color:#fff;font-size:7px;line-height:13px;text-align:center;border-radius:2px}
.links{left:453px;top:50px;font-size:8px;color:#555;line-height:14px}
.address{left:604px;top:47px;font-size:8px;color:#666;line-height:13px}
</style>
</head>
<body>

<header>
  <div class="abs brand"><span class="brand-dot"></span>Rovin Pantry</div>
  <div class="abs care">Customer Care:<strong>+61 1300 000 118</strong></div>
  <div class="abs top-link" style="left:475px">My Basket</div>
  <div class="abs top-link" style="left:665px">My Account</div>
  <div class="abs top-link" style="left:757px">Login / Register</div>
  <div class="abs basket">
    <svg width="14" height="12" viewBox="0 0 14 12"><path d="M1 4h12l-2 7H3z" fill="#3aa54a"/><path d="M4 4l3-3 3 3" stroke="#3aa54a" fill="none" stroke-width="1.4"/></svg>
  </div>
</header>

<nav class="abs nav">
  <a href="#">Home</a><a href="#">Products</a><a href="#">Recipes</a><a href="#">Contact</a>
</nav>

<aside class="abs register">
  <h3>Register</h3>
  <div class="field">Username</div>
  <div class="field">Password</div>
  <div class="field">Confirm Password</div>
  <div class="btn">REGISTER</div>
  <div class="member">Member Login</div>
</aside>

<section class="abs hero">
  <h1>Best ingredients<br>for everyday<br>kitchen fun</h1>
  <div class="hero-photo" role="img" aria-label="Stacked jars of Rovin Pantry curry powder"></div>
  <div class="play"><svg width="26" height="26" viewBox="0 0 26 26"><path d="M10 8l8 5-8 5z" fill="#fff"/></svg></div>
</section>

<h2 class="abs why-title">Why Rovin Pantry ?</h2>

<div class="abs feature" style="left:63px">
  <h4>Quality ingredient</h4>
  <div class="row">
    <svg width="22" height="22" viewBox="0 0 22 22"><rect x="2" y="4" width="16" height="16" fill="none" stroke="#3aa54a" stroke-width="2"/><path d="M6 11l4 4 10-12" fill="none" stroke="#3aa54a" stroke-width="2.6"/></svg>
    <p>Lorem ipsum dolor sit amet, consetetur sadipscing elitr, sed diam nonumy eirmod tempor invidunt ut labore et dolore magna aliquyam erat, sed diam voluptua. At vero eos et accusam et justo duo dolores et ea rebum</p>
  </div>
</div>
<div class="abs feature" style="left:336px">
  <h4>Traditional test</h4>
  <div class="row">
    <svg width="22" height="22" viewBox="0 0 22 22"><path d="M11 2L1 11h3v9h5v-6h4v6h5v-9h3z" fill="#3aa54a"/></svg>
    <p>Lorem ipsum dolor sit amet, consetetur sadipscing elitr, sed diam nonumy eirmod tempor invidunt ut labore et dolore magna aliquyam erat, sed diam voluptua. At vero eos et accusam et justo duo dolores et ea rebum</p>
  </div>
</div>
<div class="abs feature" style="left:617px">
  <h4>Confort packaging</h4>
  <div class="row">
    <svg width="24" height="22" viewBox="0 0 24 22"><path d="M2 2h20l2 6H0z" fill="#3aa54a"/><rect x="3" y="10" width="18" height="10" fill="none" stroke="#3aa54a" stroke-width="2"/><rect x="6" y="12" width="5" height="8" fill="#3aa54a"/></svg>
    <p>Lorem ipsum dolor sit amet, consetetur sadipscing elitr, sed diam nonumy eirmod tempor invidunt ut labore et dolore magna aliquyam erat, sed diam voluptua. At vero eos et accusam et justo duo dolores et ea rebum</p>
  </div>
</div>

<section class="abs products">
  <h2>Now making cury is quick &amp; easy with Rovin Pantry</h2>

  <article class="card" style="left:40px">
    <div class="shot">
      <div class="pic" role="img" aria-label="Pyramid of curry powder jars" style="background:radial-gradient(ellipse at 50% 60%,#8c6a4a,#3a2a20 70%)"></div>
      <div class="caption">Rovin Pantry Curry Powder 100gms</div>
    </div>
    <div class="price">AU$ 10.00</div>
    <div class="more">Read more <svg width="12" height="12" viewBox="0 0 12 12"><path d="M1 1l10 5-10 5 3-5z" fill="#fff"/></svg></div>
  </article>

  <article class="card" style="left:292px">
    <div class="shot">
      <div class="pic" role="img" aria-label="Open cook book on a patterned cloth" style="background:linear-gradient(160deg,#e9e4da,#b24a2a 60%,#6d2316)"></div>
      <div class="caption">Rovin Pantry Authentic Cook Book</div>
    </div>
    <div class="price">AU$ 05.00</div>
    <div class="more">Read more <svg width="12" height="12" viewBox="0 0 12 12"><path d="M1 1l10 5-10 5 3-5z" fill="#fff"/></svg></div>
  </article>

  <article class="card" style="left:544px">
    <div class="shot">
      <div class="pic" role="img" aria-label="Cook book beside a pouch of curry powder" style="background:linear-gradient(90deg,#eeeae4 45%,#8a5a2c 55%,#6a4020)"></div>
      <div class="caption">Rovin Pantry Curry Powder &amp;<br>'Table of Spice' Cook Book Combo</div>
    </div>
    <div class="price">AU$ 15.00</div>
    <div class="more">Read more <svg width="12" height="12" viewBox="0 0 12 12"><path d="M1 1l10 5-10 5 3-5z" fill="#fff"/></svg></div>
  </article>
</section>

<h2 class="abs news-title">Sign up to newsletter</h2>
<div class="abs news-input">Enter your email</div>
<div class="abs news-btn">Subscribe</div>

<footer class="abs footer">
  <div class="abs foot-head" style="left:44px">TWEETZ</div>
  <div class="abs foot-head" style="left:227px">Rovin Pantry on Social</div>
  <div class="abs foot-head" style="left:453px">QUICK LINKS</div>
  <div class="abs foot-rule" style="left:453px;width:364px"></div>

  <div class="abs tweet" style="top:42px">duo dolores et ea rebum. Stet<br><span class="url">rovin.example/a1</span><br><span class="when">16 hours ago</span></div>
  <div class="abs tweet" style="top:78px">duo dolores et ea rebum. Stet<br><span class="url">rovin.example/a1</span><br><span class="when">23 hours ago</span></div>
  <div class="abs tweet" style="top:114px">duo dolores et ea rebum. Stet<br><span class="url">rovin.example/a1</span><br><span class="when">22 May 2015</span></div>

  <div class="abs fb-box">
    <div class="avatars">
      <div class="avatar"><span role="img" aria-label="Follower photo"></span>Ravi</div>
      <div class="avatar"><span role="img" aria-label="Follower photo"></span>Mina</div>
      <div class="avatar"><span role="img" aria-label="Follower photo"></span>Lena</div>
      <div class="avatar"><span role="img" aria-label="Follower photo"></span>Devi</div>
      <div class="avatar"><span role="img" aria-label="Follower photo"></span>Anu</div>
    </div>
    <div class="fb-note">Social plugin</div>
    <div class="like">Like</div>
  </div>

  <div class="abs links">About us<br>Disclaimer<br>Terms &amp; Conditions<br>Privacy Policy</div>
  <div class="abs address">PO BOX 12 Larkfield Road<br>Ambervale, New South Wales, Australia<br><br>All rights reserved @ Rovin Pantry 2015</div>
</footer>

</body>
</html>
```